New For Sale Signs

We are looking for a design not too dissimilar to the attached. Looking more for tweaks than a radically new concept. The attached just isn't quite right. Looking to add a touch more grey (our secondary colour). We look forward to seeing your new designs!

Thank you so much for all of your creative input. We have now found the perfect design but very much appreciate your participation and wish you all the best. Kind regards, Rosalind Pemberly Brightwell Estate Agents

```html
<!DOCTYPE html>
<html lang="en">
<head>
<meta charset="utf-8">
<title>Brightwell Estate Agents – For Sale Sign</title>
<link href="https://fonts.googleapis.com/css2?family=Arimo:wght@400&display=swap" rel="stylesheet">
<style>
  :root {
    --navy: #025a7a;
    --grey: #a5acb5;
    --grey-light: #b5bcc4;
    --white: #ffffff;
    --backdrop: #e9e7e3;
  }
  * { margin: 0; padding: 0; box-sizing: border-box; }
  html, body {
    width: 957px;
    height: 1200px;
    overflow: hidden;
    background: var(--backdrop);
  }
  .sign {
    position: absolute;
    left: 143px;
    top: 97px;
    width: 670px;
    height: 1003px;
    background: var(--navy);
    font-family: "Arimo", Arial, sans-serif;
    font-weight: 400;
    color: var(--white);
    overflow: hidden;
  }
  .sign > * {
    position: absolute;
    left: 0;
    width: 100%;
    text-align: center;
    line-height: 1;
    white-space: nowrap;
  }
  .brand-name {
    top: 105px;
    font-size: 88px;
    letter-spacing: 0.01em;
  }
  .brand-tagline {
    top: 209px;
    font-size: 28px;
    letter-spacing: 0.2em;
  }
  .skyline {
    top: 278px;
    height: 273px;
  }
  .skyline svg { display: block; width: 100%; height: 100%; }
  .sale-band {
    top: 551px;
    height: 165px;
    background: var(--grey);
  }
  .sale-title {
    top: 568px;
    font-size: 140px;
    color: var(--navy);
    letter-spacing: -0.01em;
  }
  .slogan {
    top: 723px;
    font-size: 76px;
    color: var(--grey);
    letter-spacing: -0.03em;
  }
  .enquiry-note {
    top: 799px;
    font-size: 20px;
    color: var(--grey-light);
  }
  .phone {
    top: 816px;
    font-size: 114px;
    letter-spacing: -0.01em;
  }
  .website {
    top: 932px;
    font-size: 38px;
    color: var(--grey-light);
  }
</style>
</head>
<body>
  <main class="sign">
    <div class="brand-name">BRIGHTWELL</div>
    <div class="brand-tagline">ESTATE AGENTS</div>
    <div class="skyline" role="img" aria-label="Faint geometric house shapes decoration">
      <svg viewBox="0 0 670 273" preserveAspectRatio="none">
        <defs>
          <linearGradient id="skyline-fade" x1="0" y1="0" x2="0" y2="1">
            <stop offset="0" stop-color="#025a7a"/>
            <stop offset="1" stop-color="#4f7f95"/>
          </linearGradient>
        </defs>
        <rect width="670" height="273" fill="url(#skyline-fade)"/>
      </svg>
    </div>
    <div class="sale-band"></div>
    <div class="sale-title">For Sale</div>
    <div class="slogan">Home.Together.</div>
    <div class="enquiry-note">For further information regarding this property please call</div>
    <div class="phone">4397 2610</div>
    <div class="website">brightwellestateagents.com.au</div>
  </main>
</body>
</html>
```